Pomme Sauvage Riding School Flyer Design

We need a flyer for our Horse riding school, called Pomme Sauvage Riding School.

At Pomme Sauvage Riding School, Horses and ponies are carefully matched to suit each rider's experience, ability and confidence. I am a Qualified instructor, equipped to train all levels from nervous beginners to the more advanced.

Horse riding is fun! Riders, particularly children, are taught not only skills on the horse, but skills that are integral to good horsemanship and ownership of horses.

We regularly host Ladies Days, Guest Instructors, 1 hour Trail Rides and Pony Ride Days!

We teach people how to interact safely with, and care for horses so they develop a genuine love and respect for the animals and the sport.

In addition to fundamental riding techniques including walk, trot, and canter, we teach our students:
Grooming and Care of horses, Safety around horses, Balance and Co-Ordination, How to saddle up and care for Tack, Responsibility for equipment and horse, Confidence and Confidence Building for all Ages.

Private and group lessons start at 5 years of age upwards.

We recommend children 4 years and under partake in 15 minute pony rides, mainly due to their attention span!

```html
<!DOCTYPE html>
<html lang="en">
<head>
<meta charset="utf-8">
<title>Pomme Sauvage Riding School Flyer</title>
<link href="https://fonts.googleapis.com/css2?family=Amaranth:wght@400&family=Raleway:wght@500&display=swap" rel="stylesheet">
<style>
  :root {
    --backdrop: #e6e2dc;
    --forest: #2f4431;
    --forest-deep: #283b2a;
    --leaf: #a9cb4c;
    --band: #4b6a30;
    --white: #ffffff;
    --ink: #1b1b1b;
    --frame-green: #7f9a3a;
  }
  * { margin: 0; padding: 0; box-sizing: border-box; }
  html, body {
    width: 1200px; height: 905px; overflow: hidden;
    background: var(--backdrop);
  }
  .flyer {
    position: absolute; left: 20px; top: 47px;
    width: 1160px; height: 811px;
    background: linear-gradient(160deg, var(--forest) 0%, var(--forest-deep) 100%);
    overflow: hidden;
    font-family: "Amaranth", sans-serif;
    font-weight: 400;
    color: var(--white);
  }
  h2 { font-weight: 400; }
  .brand-corner { position: absolute; left: 0; top: 0; width: 460px; height: 360px; }
  .brand-mark {
    position: absolute; left: 100px; top: 48px;
    width: 54px; height: 54px; border-radius: 50%;
    background: var(--ink);
  }
  .brand-name {
    position: absolute; left: 4px; top: 150px; width: 246px;
    font-family: "Raleway", sans-serif; font-weight: 500;
    color: var(--ink); text-align: center;
  }
  .brand-name__main { display: block; font-size: 21px; letter-spacing: 2.5px; line-height: 1.3; }
  .brand-name__sub { display: block; font-size: 13px; letter-spacing: 3px; margin-top: 6px; }
  .intro-title {
    position: absolute; left: 560px; width: 460px; top: 23px;
    text-align: center; color: var(--leaf); font-size: 21.5px;
  }
  .intro-text {
    position: absolute; left: 445px; top: 50px; width: 640px;
    font-size: 18.5px; line-height: 23.6px;
  }
  .care-text {
    position: absolute; left: 290px; top: 166px; width: 592px;
    color: var(--leaf); font-size: 18.5px; line-height: 23.6px;
  }
  .skills-title {
    position: absolute; left: 48px; top: 299px; width: 560px;
    color: var(--leaf); font-size: 22.5px; line-height: 29px;
  }
  .skills-list {
    position: absolute; left: 16px; top: 372px; list-style: none;
    font-size: 18.5px; line-height: 23.6px;
  }
  .skills-list li { display: flex; align-items: center; gap: 10px; }
  .skills-list svg { width: 16px; height: 16px; flex: none; }
  .photo { position: absolute; width: 125px; height: 124px; }
  .photo--white { border: 2px solid var(--white); }
  .photo--green { border: 2px solid var(--frame-green); }
  .fun-title {
    position: absolute; left: 755px; width: 390px; top: 373px;
    text-align: center; color: var(--leaf); font-size: 21.5px;
  }
  .fun-text {
    position: absolute; left: 755px; width: 390px; top: 399px;
    text-align: center; font-size: 18.5px; line-height: 23.6px;
  }
  .horse-photo {
    position: absolute; left: 736px; top: 519px; width: 424px; height: 292px;
    background:
      radial-gradient(ellipse 55% 50% at 45% 55%, #8a4a25 0%, #a45a2c 35%, rgba(120,140,90,0.7) 70%, rgba(47,68,49,0) 100%),
      linear-gradient(180deg, rgba(47,68,49,0) 0%, rgba(111,138,82,0.6) 70%, #7f965c 100%);
  }
  .lessons-note {
    position: absolute; left: 849px; width: 240px; top: 509px;
    text-align: center; color: var(--leaf); font-size: 18.5px; line-height: 23.6px;
  }
  .ask-note {
    position: absolute; left: 203px; width: 400px; top: 543px;
    text-align: center; font-size: 18px; line-height: 23.6px;
  }
  .footer-band {
    position: absolute; left: 0; top: 731px; width: 780px; height: 80px;
    background: linear-gradient(90deg, var(--band) 85%, rgba(75,106,48,0) 100%);
  }
  .footer-text {
    position: absolute; left: 0; width: 806px; top: 742px;
    text-align: center; font-size: 21.5px; line-height: 28px;
  }
</style>
</head>
<body>
<main class="flyer">
  <svg class="brand-corner" viewBox="0 0 460 360" aria-hidden="true">
    <path d="M0 0 H432 C436 60 400 100 360 130 C320 160 282 182 278 212 C240 245 170 250 100 270 C55 285 22 312 0 344 Z" fill="var(--white)"/>
    <path d="M432 0 C436 60 400 100 360 130 C320 160 282 182 278 212" fill="none" stroke="var(--ink)" stroke-width="7" stroke-linecap="round"/>
    <path d="M278 214 C240 247 170 252 100 272 C55 287 22 314 0 346" fill="none" stroke="var(--ink)" stroke-width="8" stroke-linecap="round"/>
  </svg>
  <span class="brand-mark" aria-hidden="true"></span>
  <p class="brand-name"><span class="brand-name__main">POMME SAUVAGE</span><span class="brand-name__sub">RIDING SCHOOL</span></p>

  <h2 class="intro-title">At Pomme Sauvage Riding School</h2>
  <p class="intro-text">Horses and ponies are carefully matched to suit each rider's experience, ability and confidence. I am a Qualified instructor, tutoring from nervous beginners to the more advanced.</p>
  <p class="care-text">I teach people how to interact safely with, and care for horses as so to develop a genuine love and respect for the animals and the sport.</p>

  <h2 class="skills-title">In addition to fundamental riding techniques including walk, trot, and canter, we teach our students:</h2>
  <ul class="skills-list">
    <li><svg viewBox="0 0 16 16"><g fill="var(--leaf)"><rect x="6" y="1" width="4" height="4" transform="rotate(45 8 3)"/><rect x="6" y="11" width="4" height="4" transform="rotate(45 8 13)"/><rect x="1" y="6" width="4" height="4" transform="rotate(45 3 8)"/><rect x="11" y="6" width="4" height="4" transform="rotate(45 13 8)"/></g></svg>Grooming and Care of horses</li>
    <li><svg viewBox="0 0 16 16"><g fill="var(--leaf)"><rect x="6" y="1" width="4" height="4" transform="rotate(45 8 3)"/><rect x="6" y="11" width="4" height="4" transform="rotate(45 8 13)"/><rect x="1" y="6" width="4" height="4" transform="rotate(45 3 8)"/><rect x="11" y="6" width="4" height="4" transform="rotate(45 13 8)"/></g></svg>Safety around horses</li>
    <li><svg viewBox="0 0 16 16"><g fill="var(--leaf)"><rect x="6" y="1" width="4" height="4" transform="rotate(45 8 3)"/><rect x="6" y="11" width="4" height="4" transform="rotate(45 8 13)"/><rect x="1" y="6" width="4" height="4" transform="rotate(45 3 8)"/><rect x="11" y="6" width="4" height="4" transform="rotate(45 13 8)"/></g></svg>Balance and Co-Ordination</li>
    <li><svg viewBox="0 0 16 16"><g fill="var(--leaf)"><rect x="6" y="1" width="4" height="4" transform="rotate(45 8 3)"/><rect x="6" y="11" width="4" height="4" transform="rotate(45 8 13)"/><rect x="1" y="6" width="4" height="4" transform="rotate(45 3 8)"/><rect x="11" y="6" width="4" height="4" transform="rotate(45 13 8)"/></g></svg>How to saddle up and care for Tack</li>
    <li><svg viewBox="0 0 16 16"><g fill="var(--leaf)"><rect x="6" y="1" width="4" height="4" transform="rotate(45 8 3)"/><rect x="6" y="11" width="4" height="4" transform="rotate(45 8 13)"/><rect x="1" y="6" width="4" height="4" transform="rotate(45 3 8)"/><rect x="11" y="6" width="4" height="4" transform="rotate(45 13 8)"/></g></svg>Responsibility for equipment and horse</li>
    <li><svg viewBox="0 0 16 16"><g fill="var(--leaf)"><rect x="6" y="1" width="4" height="4" transform="rotate(45 8 3)"/><rect x="6" y="11" width="4" height="4" transform="rotate(45 8 13)"/><rect x="1" y="6" width="4" height="4" transform="rotate(45 3 8)"/><rect x="11" y="6" width="4" height="4" transform="rotate(45 13 8)"/></g></svg>Confidence and Confidence Building for all Ages.</li>
  </ul>

  <div class="photo photo--white" style="left:792px;top:236px;background:linear-gradient(160deg,#6b7a4a,#5a3a24 55%,#d8d6cc);" role="img" aria-label="Photo of the instructor standing beside a brown horse"></div>
  <div class="photo photo--white" style="left:977px;top:236px;background:linear-gradient(180deg,#b9cde0,#6f8a4a 45%,#a08a5a 80%,#6a4a2a);" role="img" aria-label="Photo of riders on a trail ride through bushland"></div>

  <h2 class="fun-title">Horse riding is fun! Riders,</h2>
  <p class="fun-text">particularly children are taught not only skills on the horse, but skills that are integral to good horsemanship and ownership of horses.</p>

  <div class="horse-photo" role="img" aria-label="Photo of a brown and white pinto horse cantering in a paddock"></div>
  <p class="lessons-note">Private, group lessons and trail rides available, All ages catered for!</p>

  <p class="ask-note">Ask about Ladies Days, Guest Instructors,<br>Trail Rides and Pony Rides</p>

  <div class="photo photo--green" style="left:41px;top:605px;background:linear-gradient(160deg,#7a8a5a,#2f3f5a 50%,#8a5a3a);" role="img" aria-label="Photo of a rider in a helmet next to a horse"></div>
  <div class="photo photo--green" style="left:217px;top:605px;background:linear-gradient(180deg,#9aa27a,#6a5a4a 50%,#b09a7a);" role="img" aria-label="Photo of a young rider on a pony in an arena with barrels"></div>
  <div class="photo photo--green" style="left:393px;top:605px;background:linear-gradient(180deg,#8a7a5a,#c0c4c8 45%,#5a3a2a);" role="img" aria-label="Photo of a small child riding a pony"></div>
  <div class="photo photo--green" style="left:564px;top:605px;background:linear-gradient(180deg,#a8c4d8,#2a2f3f 45%,#5a3a24);" role="img" aria-label="Photo of a rider in a helmet with a bay horse"></div>

  <div class="footer-band"></div>
  <p class="footer-text">We host ladies days, guest instructors, trail rides<br>and pony rides there instead?</p>
</main>
</body>
</html>
```